Brivane - Business Cards for a new venture

create business card for a startup classified business dealing in construction materials, the cards need to have a professional look but modern, more serious than playful, one of the samples must include the official font (attached), please explore using the official colors in the company's logo

Target Market(s)

Energy sector

Contact Information for Business Card

Font styles to use
Other font styles liked:
• suissnord

Requirements
Must have
• corporate colors (in logo attached)
Nice to have
• Official font (in one of the samples) font is : suissnord
Should not have
• Cartoonish look

```html
<!DOCTYPE html>
<html lang="en">
<head>
<meta charset="utf-8">
<title>Brivane – Business Cards</title>
<link rel="stylesheet" href="https://fonts.googleapis.com/css2?family=Michroma&family=Questrial&display=swap">
<style>
  :root {
    --page: #ffffff;
    --card-dark: #0a0a0a;
    --card-glow: #3a3d40;
    --band-red: #650404;
    --accent-red: #6a0a0a;
    --tile-white: #ffffff;
    --tile-grey: #98a1a6;
    --brand-blue: #0d3a8f;
    --text-grey: #a4adb2;
  }
  html, body {
    margin: 0;
    padding: 0;
    width: 1200px;
    height: 1077px;
    overflow: hidden;
    background: var(--page);
  }
  .sheet {
    position: relative;
    width: 1200px;
    height: 1077px;
  }

  /* Front of card */
  .card-front {
    position: absolute;
    left: 0;
    top: 112px;
    width: 774px;
    height: 441px;
    background: radial-gradient(ellipse 300px 260px at 384px 90px, var(--card-glow) 0%, #16181a 55%, var(--card-dark) 100%);
    overflow: hidden;
  }
  .front-band {
    position: absolute;
    left: 0;
    top: 155px;
    width: 774px;
    height: 105px;
    background: var(--band-red);
  }
  .tile-shadow {
    position: absolute;
    left: 215px;
    top: 84px;
    width: 330px;
    height: 240px;
    background: var(--tile-grey);
    transform: rotate(3.5deg);
  }
  .brand-tile {
    position: absolute;
    left: 222px;
    top: 91px;
    width: 319px;
    height: 223px;
    background: var(--tile-white);
    display: flex;
    flex-direction: column;
    align-items: center;
    justify-content: center;
    gap: 26px;
  }
  .brand-square {
    width: 46px;
    height: 46px;
    background: var(--brand-blue);
  }
  .brand-name {
    font-family: "Michroma", sans-serif;
    font-size: 22px;
    letter-spacing: 3px;
    color: var(--tile-grey);
    margin: 0;
  }

  /* Back of card */
  .card-back {
    position: absolute;
    left: 426px;
    top: 634px;
    width: 774px;
    height: 443px;
    background: var(--card-dark);
  }
  .accent-rule {
    position: absolute;
    left: 65px;
    top: 77px;
    width: 7px;
    height: 288px;
    background: var(--accent-red);
  }
  .holder-name {
    position: absolute;
    left: 93px;
    top: 82px;
    margin: 0;
    font-family: "Michroma", sans-serif;
    font-weight: 400;
    font-size: 31px;
    letter-spacing: 1px;
    line-height: 1;
    color: var(--text-grey);
  }
  .holder-role {
    position: absolute;
    left: 93px;
    top: 124px;
    margin: 0;
    font-family: "Questrial", sans-serif;
    font-size: 26px;
    color: var(--text-grey);
    letter-spacing: 0.5px;
  }
  .contact-list {
    position: absolute;
    left: 93px;
    top: 218px;
    margin: 0;
    padding: 0;
    list-style: none;
    font-family: "Questrial", sans-serif;
    font-size: 20px;
    line-height: 27.5px;
    color: var(--text-grey);
  }
</style>
</head>
<body>
<main class="sheet">
  <section class="card-front" aria-label="Card front">
    <div class="front-band"></div>
    <div class="tile-shadow"></div>
    <div class="brand-tile">
      <div class="brand-square"></div>
      <p class="brand-name">BRIVANE</p>
    </div>
  </section>

  <section class="card-back" aria-label="Card back">
    <div class="accent-rule"></div>
    <h1 class="holder-name">MR. BRIVANE</h1>
    <p class="holder-role">Chief Executive Officer</p>
    <ul class="contact-list">
      <li>Mobile: (+61) 0400 555 182</li>
      <li>Office: Head</li>
      <li>Email: mr.brivane@brivane.com</li>
      <li>Address: Level 3, 18 Ferrow Lane, Darlinghurst 2010 NSW Australia</li>
    </ul>
  </section>
</main>
</body>
</html>
```